Law Firm Stationery/Cards
Penhallow & Birchmont
Law Firm Stationery/Cards -
Creative Brief
Use specific fonts
Use whatever fonts look best
Professional
Martin K. Birchmont
Attorney at Law
7150 E. Marlow Avenue Suite 230 Tampa, FL 33614
mbirchmont@bayinjurylawgroup.com
www.bayinjurylawgroup.com
Include in business card: Social Security Disability Board Certified in Workers' Compensation Stationery/Letterhead should include Attorney names: Daniel T. Penhallow* Martin K. Birchmont* * Board Certified in Workers' Compensation Attorney include the practice areas "Social Security Disability" and "Workers' Compensation" on the letterhead We'd like it to be flexible for adding additional office locations or additional attorneys in the future. I'll upload our current letterhead for informational purposes only - not design.
Designer's choice

```html
<!DOCTYPE html>
<html lang="en">
<head>
<meta charset="utf-8">
<title>Penhallow &amp; Birchmont — Stationery</title>
<link href="https://fonts.googleapis.com/css2?family=Cinzel:wght@500&family=EB+Garamond:wght@400;500&display=swap" rel="stylesheet">
<style>
  :root {
    --backdrop: #6b6b6d;
    --paper: #ffffff;
    --gold: #8f6a2a;
    --ink: #3d3d3d;
    --muted: #9a9a9a;
    --rule: #b8b8b8;
    --shadow: rgba(0,0,0,0.35);
  }
  * { margin: 0; padding: 0; box-sizing: border-box; }
  html, body { width: 1200px; height: 871px; overflow: hidden; }
  body { background: var(--backdrop); position: relative; font-family: "EB Garamond", Georgia, serif; color: var(--ink); }

  .card, .letterhead { position: absolute; background: var(--paper); box-shadow: 2px 3px 8px var(--shadow); }
  .card { left: 72px; width: 437px; height: 266px; border-radius: 20px; }
  .card-front { top: 240px; }
  .card-back { top: 533px; }
  .letterhead { left: 552px; top: 84px; width: 583px; height: 720px; }

  .brand { position: absolute; display: flex; align-items: center; }
  .brand-square { background: var(--gold); flex: none; }
  .brand-rule { width: 1px; background: var(--rule); align-self: stretch; }
  .brand-name { font-family: "Cinzel", "Times New Roman", serif; font-weight: 500; color: var(--gold); letter-spacing: 0.02em; line-height: 1; white-space: nowrap; }
  .brand-tagline { font-family: "EB Garamond", Georgia, serif; color: var(--gold); letter-spacing: 0.12em; text-transform: uppercase; line-height: 1; }

  .card-front .brand { left: 22px; top: 30px; height: 62px; gap: 14px; }
  .card-front .brand-square { width: 44px; height: 44px; }
  .card-front .brand-name { font-size: 21px; }
  .card-front .brand-tagline { font-size: 10px; margin-top: 7px; }

  .person { position: absolute; left: 96px; top: 92px; }
  .person-name { font-size: 22px; line-height: 1.1; color: var(--ink); }
  .person-title { font-size: 14px; color: var(--muted); margin-top: 2px; }
  .stars { display: flex; gap: 16px; margin: 9px 0 10px 3px; }
  .stars span { width: 6px; height: 6px; background: var(--muted); transform: rotate(45deg); }
  .contact { font-size: 11.5px; line-height: 17px; color: var(--muted); }

  .card-back .mark-row { position: absolute; left: 0; right: 0; top: 40px; height: 90px; display: flex; align-items: center; justify-content: center; gap: 34px; }
  .mark-row .dot { width: 11px; height: 11px; background: var(--rule); transform: rotate(45deg); }
  .mark-row .brand-name { font-size: 15px; }
  .card-back .band { position: absolute; left: 0; right: 0; top: 200px; border-top: 1px solid var(--rule); }
  .card-back .practice { position: absolute; left: 17px; top: 216px; font-size: 14.5px; color: var(--ink); white-space: nowrap; }

  .letterhead .brand { left: 24px; top: 12px; height: 32px; gap: 9px; }
  .letterhead .brand-square { width: 26px; height: 26px; }
  .letterhead .brand-name { font-size: 13px; }
  .letterhead .brand-tagline { font-size: 6px; margin-top: 4px; }
  .attorneys { position: absolute; left: 24px; top: 60px; }
  .attorneys p { font-size: 12px; line-height: 17px; color: var(--ink); }
  .attorneys .stars { gap: 10px; margin: 6px 0 6px 2px; }
  .attorneys .stars span { width: 4px; height: 4px; }
  .attorneys .note { font-size: 8px; color: var(--muted); }
  .footer { position: absolute; left: 24px; top: 634px; font-size: 6.5px; line-height: 12px; color: var(--muted); }
  .seal { position: absolute; left: 526px; top: 628px; }
</style>
</head>
<body>

<section class="card card-front" aria-label="Business card, front">
  <div class="brand">
    <div class="brand-square"></div>
    <div class="brand-rule"></div>
    <div>
      <div class="brand-name">Penhallow &amp; Birchmont</div>
      <div class="brand-tagline">Attorneys at Law</div>
    </div>
  </div>
  <div class="person">
    <p class="person-name">Martin K. Birchmont</p>
    <p class="person-title">Attorney at Law</p>
    <div class="stars"><span></span><span></span><span></span><span></span><span></span></div>
    <p class="contact">Phone: 813.555.0142 | Fax: 813.555.0143</p>
    <p class="contact">mbirchmont@bayinjurylawgroup.com</p>
    <p class="contact">www.bayinjurylawgroup.com</p>
    <p class="contact">7150 E. Marlow Avenue | Suite 230 | Tampa, FL 33614</p>
  </div>
</section>

<section class="card card-back" aria-label="Business card, back">
  <div class="mark-row">
    <span class="dot"></span>
    <span class="dot"></span>
    <span class="brand-name">Penhallow &amp; Birchmont</span>
    <span class="dot"></span>
    <span class="dot"></span>
  </div>
  <div class="band"></div>
  <p class="practice">Social Security Disability | Board Certified Worker’s Compensation</p>
</section>

<section class="letterhead" aria-label="Letterhead">
  <div class="brand">
    <div class="brand-square"></div>
    <div>
      <div class="brand-name">Penhallow &amp; Birchmont</div>
      <div class="brand-tagline">Attorneys at Law</div>
    </div>
  </div>
  <div class="attorneys">
    <p>Daniel T. Penhallow*</p>
    <p>Martin K. Birchmont*</p>
    <div class="stars"><span></span><span></span><span></span><span></span></div>
    <p class="note">*Board Certified Worker’s Compensation</p>
  </div>
  <div class="footer">
    <p>7150 E. Marlow Avenue | Suite 230 | Tampa, FL 33614 | Phone: 813.555.0142 | Fax: 813.555.0143</p>
    <p>mbirchmont@bayinjurylawgroup.com | info@bayinjurylawgroup.com | www.bayinjurylawgroup.com</p>
  </div>
  <svg class="seal" width="30" height="30" viewBox="0 0 30 30" aria-hidden="true">
    <circle cx="15" cy="15" r="13" fill="none" stroke="#9a9a9a" stroke-width="1.2"/>
  </svg>
</section>

</body>
</html>
```